Construction Company

Design a clutter free business card, it can be double-sided utilizing the logo for BDN Ltd simple with all relevant contact information.

Please also a letterhead design to function for the purposes of invoicing, all mail requirements, with header to be distinctive while the footer ties page together and incorporates all necessary information.

For now, please use generic / dummy text and when a winner is selected, I will disclose the contact information.

Hi Designers! Please read the updated brief which includes the design of a business card and letterhead. Thank you!

```html
<!DOCTYPE html>
<html lang="en">
<head>
<meta charset="UTF-8">
<title>BDN Ltd Business Card</title>
<link rel="stylesheet" href="https://fonts.googleapis.com/css2?family=Bebas+Neue&family=Arimo:wght@400;700&display=swap">
<style>
  :root {
    --backdrop: #0b0b0b;
    --card: #1a1a1a;
    --gold: #c9a01e;
    --text-light: #bdbdbd;
    --rule: #5a5a5a;
  }
  html, body {
    margin: 0;
    padding: 0;
    width: 1200px;
    height: 900px;
    overflow: hidden;
    background: var(--backdrop);
  }
  .canvas {
    position: relative;
    width: 1200px;
    height: 900px;
  }
  .card {
    position: absolute;
    left: 320px;
    width: 560px;
    height: 320px;
    background: var(--card);
    box-shadow: 0 10px 30px rgba(0,0,0,0.6);
    overflow: hidden;
  }
  .card-front { top: 80px; }
  .card-back { top: 480px; }

  .brand {
    position: absolute;
    left: 0;
    right: 0;
    top: 128px;
    display: flex;
    align-items: center;
    justify-content: center;
    gap: 14px;
  }
  .brand-dot {
    width: 26px;
    height: 26px;
    border-radius: 50%;
    background: var(--gold);
  }
  .brand-name {
    font-family: "Arimo", Arial, sans-serif;
    font-weight: 700;
    font-size: 48px;
    letter-spacing: 2px;
    color: var(--gold);
    line-height: 1;
  }

  .identity {
    position: absolute;
    right: 300px;
    top: 96px;
    text-align: right;
    white-space: nowrap;
  }
  .person-name {
    font-family: "Bebas Neue", Impact, sans-serif;
    font-weight: 400;
    font-size: 40px;
    color: var(--gold);
    line-height: 1;
    margin: 0;
  }
  .person-role {
    font-family: "Arimo", Arial, sans-serif;
    font-size: 14px;
    color: var(--text-light);
    margin: 4px 0 0;
  }
  .divider {
    position: absolute;
    left: 282px;
    top: 100px;
    width: 1px;
    height: 96px;
    background: var(--rule);
  }
  .contact-list {
    position: absolute;
    left: 302px;
    top: 102px;
    margin: 0;
    padding: 0;
    list-style: none;
    font-family: "Arimo", Arial, sans-serif;
    font-size: 14px;
    color: var(--text-light);
    white-space: nowrap;
  }
  .contact-list li {
    display: flex;
    align-items: center;
    gap: 8px;
    height: 23px;
  }
  .contact-icon {
    width: 13px;
    height: 13px;
    flex: none;
  }
  .address {
    position: absolute;
    left: 100px;
    top: 252px;
    margin: 0;
    font-family: "Arimo", Arial, sans-serif;
    font-size: 14px;
    color: var(--text-light);
    white-space: nowrap;
  }
</style>
</head>
<body>
<main class="canvas">
  <section class="card card-front" aria-label="Card front">
    <div class="brand">
      <span class="brand-dot"></span>
      <span class="brand-name">BDN Ltd</span>
    </div>
  </section>

  <section class="card card-back" aria-label="Card back">
    <div class="identity">
      <h1 class="person-name">Daniel Harper</h1>
      <p class="person-role">Managing Director</p>
    </div>
    <div class="divider"></div>
    <ul class="contact-list">
      <li>
        <svg class="contact-icon" viewBox="0 0 24 24" aria-hidden="true"><path fill="var(--gold)" d="M6.6 10.8a15 15 0 0 0 6.6 6.6l2.2-2.2a1 1 0 0 1 1-.25 11.4 11.4 0 0 0 3.6.57 1 1 0 0 1 1 1V20a1 1 0 0 1-1 1A17 17 0 0 1 3 4a1 1 0 0 1 1-1h3.5a1 1 0 0 1 1 1c0 1.25.2 2.45.57 3.57a1 1 0 0 1-.25 1z"/></svg>
        055-310 482 716
      </li>
      <li>
        <svg class="contact-icon" viewBox="0 0 24 24" aria-hidden="true"><rect x="6" y="2" width="12" height="20" rx="2" fill="none" stroke="var(--gold)" stroke-width="2.5"/><circle cx="12" cy="18" r="1.3" fill="var(--gold)"/></svg>
        055-310 482 716
      </li>
      <li>
        <svg class="contact-icon" viewBox="0 0 24 24" aria-hidden="true"><rect x="2" y="5" width="20" height="14" fill="var(--gold)"/><path d="M2 5l10 8 10-8" fill="none" stroke="var(--card)" stroke-width="1.8"/></svg>
        info@bdnbuild.com
      </li>
      <li>
        <svg class="contact-icon" viewBox="0 0 24 24" aria-hidden="true"><g fill="none" stroke="var(--gold)" stroke-width="2"><circle cx="12" cy="12" r="10"/><ellipse cx="12" cy="12" rx="4.5" ry="10"/><path d="M2 12h20M4 7h16M4 17h16"/></g></svg>
        www.bdnbuild.com
      </li>
    </ul>
    <p class="address">87, Harbour Lane Business Park 31208, Northland</p>
  </section>
</main>
</body>
</html>
```